Banner Ad Design Project for Home Technology Company

We need banner ads designed for our company. See the description of what we do below the basic messages listed, section titled "ABOUT TALLWICKET"

Basic Messages:
See it. Hear it. Live it.

1. Message #1: Discover YOUR Tallwicket. Audio? Video? Media Rooms? Connected Home? We do it all!

2. Message #2: Audio
You don't need magical ears to find the perfect speakers. It's as simple as: "Which speakers sound best to you?" We can help, but it's ultimately your decision.

3. Message #3: Digital Media
- Option A: The future of how we listen to music is happening now.
- Option B: Are you just listening to your music or are you enjoying it?
- Option C: Take control of your music.
- Option D: If you aren't blown away, we aren't doing our job!

4. Message #4: Media Room
It doesn't matter where you want to watch TV & movies, enjoy your favorite music, or host parties where your guests get to be the DJ, we can help you create your ultimate entertainment zone. We've created numerous media rooms, dedicated home theaters, game rooms, and whole home entertainment systems.

5. Message #5: Connected Home
Enhance your home and your life.

ABOUT TALLWICKET:
Technology is everywhere. It’s hard to imagine any aspect of our lives that doesn’t involve it. From phones to our cars, from work to our home, technology enhances our lives, bringing us closer to information, entertainment, and each other. Often though, our different devices exist in isolation, connecting us to the world, but rarely working together to create a more elegant whole. It doesn’t have to be that way.

Imagine a home that greets you by unlocking the front door, disabling the security system, turning on lights, and welcoming you with your favorite music. Imagine a home that automatically lowers shades before the sun can fade your furniture and décor. Imagine a favorite song playing in each room of the house, or the latest hit film streaming and displayed across a wall-sized screen. Imagine prompting all of this from your smart phone.

This is only the beginning of the promise offered by an intelligent home. Beyond showcasing the latest technology, the ultimate goal is to make interaction with your home’s advanced automation features a pleasure. Exceptionally easy, yet wonderfully sophisticated, it is technology designed to help you manage your life.It’s about living in the home of the future, right now.

Here at Tallwicket we’ve helped families make complex technology simple for over 36 years. We provide advanced, professional, creative resources dedicated to ensuring your project’s success. From beautifully integrated design to the finest home technologies, we’ll guide you through each step of the design and installation process to make certain you have exactly the products you need, the features you want, and the personal attention that will make the home of the future a joy to own today.

Enhance your home and your life; let us show you how.
Updates

Brief will be completed soon. Please wait until that has been posted.  I'm setting up projects now, then adding the creative briefs.

Thank you for your patience.

Brief has been updated & Lots of information has been added.

Project Deadline Extended

Added a file with some lifestyle photos of products we sell. If you need others, please make a request.

Some lifestyle product photos of products we sell can be downloaded from this link: http://shrt.example/Xq7r

We are still looking for more designs. While we've found a few that we do like, we're still looking for more.  That's why we've extended the deadline by another week.  Please continue to submit designs as all will be considered.

Target Market(s)

English-speaking adults, aged 35-55. 60% are married; 40% have children in the household. 75% have college degrees or greater. These are innovation seekers, design & technology enthusiasts. They're interested in having premium experiences, top brands, being the first to own the latest and greatest in technology.

Industry/Entity Type

Entertainment

Requirements
Must have
- Must include only one message per banner ad set.
- Must mimic the current design style of tallwicket.example.
- Please make sure that each individual banners file size is less than 40k
Nice to have
• Button that allows viewers to click through to our website. Button should include text such as:
- Learn More
- Discover More

The above are purely examples; other calls-to-action could also work.
Should not have
• Curved Lines.

```html
<!DOCTYPE html>
<html lang="en">
<head>
<meta charset="utf-8">
<title>Tallwicket Banner Set</title>
<link href="https://fonts.googleapis.com/css2?family=Cabin+Condensed:wght@400;500&family=Arimo:wght@700&display=swap" rel="stylesheet">
<style>
  :root {
    --stage: #5b3c24;
    --ink: #1f1d1c;
    --band: #262321;
    --accent: #fbb72e;
    --paper: #f1ede4;
    --button: #2f9a32;
    --button-edge: #1f7a24;
    --white: #ffffff;
    --photo-light: #8a8a8a;
    --photo-mid: #4a4a4a;
    --photo-dark: #1c1c1c;
  }
  * { box-sizing: border-box; margin: 0; padding: 0; }
  html, body { width: 1200px; height: 1185px; overflow: hidden; }
  body {
    background: var(--stage);
    font-family: "Cabin Condensed", "Arial Narrow", sans-serif;
    position: relative;
  }
  .banner {
    position: absolute;
    background: var(--band);
    overflow: hidden;
    box-shadow: 0 3px 8px rgba(0,0,0,.45);
  }
  .photo {
    position: absolute;
    background: linear-gradient(135deg, var(--photo-light) 0%, var(--photo-mid) 45%, var(--photo-dark) 100%);
  }
  .question-strip {
    position: absolute;
    background: var(--accent);
    color: var(--ink);
    font-size: 21px;
    line-height: 30px;
    white-space: nowrap;
  }
  .claim {
    position: absolute;
    color: var(--accent);
    white-space: nowrap;
    line-height: 1;
  }
  .discover {
    position: absolute;
    color: var(--accent);
    text-align: center;
    line-height: 1.05;
  }
  .cta {
    position: absolute;
    background: var(--button);
    border: 2px solid var(--button-edge);
    color: var(--white);
    font-family: "Arimo", Arial, sans-serif;
    font-weight: 700;
    font-size: 18px;
    display: flex;
    align-items: center;
    justify-content: center;
    text-decoration: none;
  }
  .brand-panel {
    position: absolute;
    background: var(--paper);
    display: flex;
    flex-direction: column;
    align-items: center;
    justify-content: center;
  }
  .brand-dot {
    border-radius: 50%;
    background: var(--accent);
  }
  .brand-name {
    color: var(--ink);
    font-weight: 400;
    letter-spacing: 1px;
    line-height: 1;
  }

  /* leaderboard */
  .leaderboard { left: 57px; top: 57px; width: 1087px; height: 134px; }
  .leaderboard .photo { left: 463px; top: 0; width: 624px; height: 134px; }
  .leaderboard .brand-panel {
    left: 0; top: 0; width: 240px; height: 134px;
    clip-path: polygon(0 0, 100% 0, 84% 100%, 0 100%);
    padding-right: 30px;
  }
  .leaderboard .brand-dot { width: 52px; height: 52px; margin-bottom: 8px; }
  .leaderboard .brand-name { font-size: 24px; }
  .leaderboard .discover { left: 240px; top: 25px; width: 240px; font-size: 34px; }
  .leaderboard .question-strip {
    left: 463px; top: 0; width: 624px; height: 30px;
    clip-path: polygon(0 0, 100% 0, 100% 100%, 3% 100%);
    text-align: right; padding-right: 58px;
  }
  .leaderboard .claim { right: 6px; top: 38px; font-size: 37px; }
  .leaderboard .cta { left: 912px; top: 87px; width: 162px; height: 36px; }

  /* skyscraper */
  .skyscraper { left: 57px; top: 233px; width: 239px; height: 896px; }
  .skyscraper .question-stack {
    position: absolute; left: 0; top: 0; width: 239px; height: 209px;
    background: var(--accent); color: var(--ink); text-align: right;
    padding: 4px 4px 0 0; line-height: 1;
  }
  .skyscraper .q-large { font-size: 50px; display: block; text-align: center; padding-left: 20px; }
  .skyscraper .q-mid { font-size: 37px; display: block; margin-top: 4px; }
  .skyscraper .q-small { font-size: 30px; display: block; margin-top: 6px; }
  .skyscraper .claim { right: 4px; top: 225px; font-size: 43px; }
  .skyscraper .photo { left: 0; top: 284px; width: 239px; height: 358px; }
  .skyscraper .cta { left: 42px; top: 290px; width: 161px; height: 38px; }
  .skyscraper .discover { left: 0; top: 655px; width: 239px; font-size: 34px; }
  .skyscraper .brand-panel { left: 0; top: 743px; width: 239px; height: 153px; }
  .skyscraper .brand-dot { width: 72px; height: 72px; margin-bottom: 12px; }
  .skyscraper .brand-name { font-size: 29px; }

  /* medium rectangle */
  .rectangle { left: 349px; top: 233px; width: 503px; height: 418px; }
  .rectangle .question-strip { left: 0; top: 0; width: 503px; height: 30px; text-align: center; }
  .rectangle .photo { left: 0; top: 30px; width: 503px; height: 283px; }
  .rectangle .claim { right: 12px; top: 38px; font-size: 52px; }
  .rectangle .cta { left: 324px; top: 107px; width: 160px; height: 36px; }
  .rectangle .brand-panel {
    left: 0; top: 313px; width: 205px; height: 105px;
    clip-path: polygon(0 0, 100% 0, 100% 0, 100% 100%, 0 100%);
    clip-path: polygon(0 0, 82% 0, 100% 100%, 0 100%);
    padding-right: 26px;
  }
  .rectangle .brand-dot { width: 42px; height: 42px; margin-bottom: 6px; }
  .rectangle .brand-name { font-size: 21px; }
  .rectangle .discover { left: 210px; top: 325px; width: 270px; font-size: 39px; }
</style>
</head>
<body>

  <section class="banner leaderboard" aria-label="Leaderboard banner">
    <div class="photo" role="img" aria-label="Close-up photo of a studio mixing console with faders"></div>
    <div class="brand-panel">
      <span class="brand-dot"></span>
      <span class="brand-name">TALLWICKET</span>
    </div>
    <p class="discover">Discover YOUR<br>Tallwicket</p>
    <p class="question-strip">Audio? Video? Media Rooms? Connected Home?</p>
    <p class="claim">We do it all!</p>
    <a class="cta" href="#">Learn More</a>
  </section>

  <section class="banner skyscraper" aria-label="Skyscraper banner">
    <p class="question-stack">
      <span class="q-large">Audio?</span>
      <span class="q-large">Video?</span>
      <span class="q-mid">Media Rooms?</span>
      <span class="q-small">Connected home?</span>
    </p>
    <p class="claim">We do it all!</p>
    <div class="photo" role="img" aria-label="Close-up photo of a studio mixing console with faders"></div>
    <a class="cta" href="#">Learn More</a>
    <p class="discover">Discover YOUR<br>Tallwicket</p>
    <div class="brand-panel">
      <span class="brand-dot"></span>
      <span class="brand-name">TALLWICKET</span>
    </div>
  </section>

  <section class="banner rectangle" aria-label="Medium rectangle banner">
    <p class="question-strip">Audio? Video? Media Rooms? Connected Home?</p>
    <div class="photo" role="img" aria-label="Close-up photo of a studio mixing console with faders"></div>
    <p class="claim">We do it all!</p>
    <a class="cta" href="#">Learn More</a>
    <div class="brand-panel">
      <span class="brand-dot"></span>
      <span class="brand-name">TALLWICKET</span>
    </div>
    <p class="discover">Discover YOUR<br>Tallwicket</p>
  </section>

</body>
</html>
```